Business Card & Logo Design Project

I am looking for a slick/simple design for a logo and business card, for a music Producer/Mixer/Engineer.

I'm based in Tokyo, Japan and I help my clients polish up their creation to major radio/TV status. My clients pay me for my taste, sense of balance expertise and creative direction/

Design should give impression of seal of quality, professionalism, and enthusiasm need some sort of a logo like design for "vantrix productions".

Please don't include music notes or instruments or anything musically related and anything samurai or ninja or too much Japan in them on the design.

I like clever, slick stuff that's not too obvious.
I also like a smooth gradation type transition. My favorite color is deep dark blue/

Good Luck and Thank you for your effort.
Updates

I would like a two-sided design for this one.
One side with "vantrix productions" (all lower case) on, and the other side with my name and contact info.

Please also consider portrait position (or direction).  (as opposed to landscape) 

Target Market(s)

My primary targets are artists & bands, who want absolute best for their creation.

Industry/Entity Type

Business

Requirements
Must have
• Two-Sided
1, vantrix productions
2, Kenji Harumoto, Producer/Mixer/Engineer, +81 090 4827 3516, brambleway@mailnest.example
Nice to have
• Any suggestions are welcome//
Should not have
• Anything music related images.
(e.g. CD, music notations, instruments etc.)

```html
<!DOCTYPE html>
<html lang="en">
<head>
<meta charset="utf-8">
<title>vantrix productions – business card</title>
<link rel="stylesheet" href="https://fonts.googleapis.com/css2?family=Arimo:wght@400;700&display=swap">
<style>
  :root {
    --stage: #2a2a2c;
    --card-glow: #1d5f86;
    --card-mid: #134468;
    --card-edge: #0a2742;
    --ink: #ffffff;
    --shadow: rgba(0, 0, 0, 0.55);
  }
  * { margin: 0; padding: 0; box-sizing: border-box; }
  html, body {
    width: 1200px;
    height: 900px;
    overflow: hidden;
    background: var(--stage);
  }
  .canvas {
    position: relative;
    width: 1200px;
    height: 900px;
    background: var(--stage);
    font-family: "Arimo", Arial, sans-serif;
    color: var(--ink);
  }
  .card {
    position: absolute;
    width: 700px;
    height: 450px;
    background: radial-gradient(ellipse 60% 62% at 52% 50%, var(--card-glow) 0%, var(--card-mid) 48%, var(--card-edge) 100%);
    box-shadow: 0 12px 28px var(--shadow);
  }
  .card--front {
    left: 30px;
    top: 60px;
    z-index: 2;
  }
  .card--back {
    left: 470px;
    top: 400px;
    z-index: 1;
  }
  .brand-name {
    position: absolute;
    left: 170px;
    top: 205px;
    font-size: 44px;
    font-weight: 400;
    letter-spacing: 0.5px;
    color: var(--ink);
  }
  .edge-mark {
    position: absolute;
    left: 12px;
    width: 7px;
    background: var(--ink);
  }
  .edge-mark--upper { top: 135px; height: 60px; }
  .edge-mark--lower { top: 300px; height: 60px; }
  .identity {
    position: absolute;
    right: 40px;
    top: 185px;
    text-align: right;
    font-weight: 700;
    line-height: 1.05;
  }
  .identity__name {
    font-size: 36px;
    letter-spacing: 0.5px;
  }
  .identity__role {
    font-size: 27px;
  }
  .contact {
    position: absolute;
    right: 40px;
    bottom: 38px;
    text-align: right;
    font-weight: 700;
    font-size: 22px;
    line-height: 1.15;
  }
</style>
</head>
<body>
  <main class="canvas">
    <section class="card card--front" aria-label="Card front">
      <p class="brand-name">vantrix productions</p>
    </section>

    <section class="card card--back" aria-label="Card back">
      <span class="edge-mark edge-mark--upper"></span>
      <span class="edge-mark edge-mark--lower"></span>
      <div class="identity">
        <p class="identity__name">KENJI HARUMOTO</p>
        <p class="identity__role">PRODUCER/MIXER/ENGINEER</p>
      </div>
      <div class="contact">
        <p class="contact__phone">+81 090 4827 3516</p>
        <p class="contact__email">brambleway@mailnest.example</p>
      </div>
    </section>
  </main>
</body>
</html>
```